URGENT REQUEST Business Card for Executive Coach (already have logo)

Tavener Growth Advisory is a one person business doing high-end executive coaching, leadership training, and personal transformation work (psychotherapy). I urgently need new cards to fit my new logo.

I would like the card to be scannable by ScanTile and Quillbook Howdy.

A draft of the company website is at http://pruvex.net/demo/tavener

Target Market(s)

Senior corporate executives

Industry/Entity Type

Leadership

Requirements
Must have

• 1. Please use the company tag line: "The psychology of executive excellence"
2. My name is: Gregory Tavener, PhD (Kelbrook)
3. Behind my name, please make "(Kelbrook)" in smaller font.
4. My Title: Executive Coach & Leadership Trainer
4. No street address
5. If there is space, please put my current appointments:
Leadership Studies Faculty (CPA)
Supervisor & Coach (VORTEK)
6. Email: Gtavgreg@TavenerAdvisory.net
7. Web: www.TavenerAdvisory.net
8. Mobile: +65 8456-0000
Nice to have
• Company Tag Line:
• The psychology of executive excellence and personal transformation
• What I provide:
• Executive Coaching
• Leadership Training
• Personal Transformation

```html
<!DOCTYPE html>
<html lang="en">
<head>
<meta charset="utf-8">
<title>Tavener Growth Advisory — Business Card</title>
<link rel="stylesheet" href="https://fonts.googleapis.com/css2?family=Audiowide&family=Raleway:wght@700&family=Tinos&display=swap">
<style>
  :root {
    --bg: #3a2e38;
    --card: #f4f4f5;
    --card-shade: #d9d9dc;
    --brand-red: #9e1b1f;
    --bar-red: #a3161c;
    --ink: #1c1c1c;
    --ink-soft: #333;
    --white: #ffffff;
  }
  * { box-sizing: border-box; margin: 0; padding: 0; }
  html, body { width: 1200px; height: 800px; overflow: hidden; }
  body {
    background: var(--bg);
    display: flex;
    align-items: center;
    justify-content: center;
    gap: 60px;
  }
  .card {
    position: relative;
    width: 525px;
    height: 300px;
    background: var(--card);
    box-shadow: 0 12px 30px rgba(0,0,0,.35);
    overflow: hidden;
  }
  .card--back {
    background: linear-gradient(180deg, var(--card-shade) 0 40%, var(--card) 40% 100%);
  }
  .card--front {
    background: linear-gradient(160deg, var(--white), var(--card) 60%, var(--card-shade));
  }
  .brand {
    position: absolute;
    top: 26px;
    left: 26px;
    display: flex;
    align-items: center;
    gap: 8px;
  }
  .brand__mark {
    width: 12px;
    height: 12px;
    background: var(--brand-red);
  }
  .brand__name {
    font-family: "Tinos", serif;
    font-size: 21px;
    line-height: 1.1;
    color: var(--brand-red);
    white-space: nowrap;
  }
  .person {
    position: absolute;
    top: 72px;
    left: 26px;
  }
  .person__name {
    font-family: "Tinos", serif;
    font-size: 17px;
    color: var(--ink);
  }
  .person__school { font-size: 9px; letter-spacing: .5px; text-transform: uppercase; }
  .person__appointment {
    font-family: "Tinos", serif;
    font-size: 9.5px;
    color: var(--ink-soft);
    line-height: 1.25;
  }
  .contact {
    position: absolute;
    top: 150px;
    left: 26px;
    list-style: none;
    font-family: "Tinos", serif;
    font-size: 11.5px;
    color: var(--ink);
  }
  .contact li { display: flex; gap: 16px; line-height: 1.65; }
  .contact__key { width: 10px; }
  .role {
    font-family: "Audiowide", sans-serif;
    color: var(--brand-red);
    text-shadow: 1px 1px 0 #2a0a0b, 2px 2px 1px rgba(0,0,0,.45);
    text-transform: uppercase;
  }
  .role--stacked {
    position: absolute;
    top: 150px;
    right: 40px;
    width: 170px;
    text-align: center;
    font-size: 12px;
    line-height: 2.1;
  }
  .role--headline {
    position: absolute;
    top: 100px;
    left: 26px;
    right: 26px;
    font-size: 24px;
    letter-spacing: .5px;
  }
  .tagline {
    position: absolute;
    right: 22px;
    bottom: 26px;
    background: var(--bar-red);
    color: var(--white);
    font-family: "Raleway", sans-serif;
    font-weight: 700;
    font-size: 11px;
    text-transform: uppercase;
    padding: 5px 10px;
    letter-spacing: .2px;
    white-space: nowrap;
  }
</style>
</head>
<body>
  <section class="card card--back" aria-label="Card back with contact details">
    <div class="brand">
      <span class="brand__mark"></span>
      <span class="brand__name">Tavener Growth Advisory</span>
    </div>
    <div class="person">
      <p class="person__name">Gregory Tavener, PhD <span class="person__school">Kelbrook</span></p>
      <p class="person__appointment">Leadership Studies Faculty (CPA)</p>
      <p class="person__appointment">Supervisor &amp; Coach (VORTEK)</p>
    </div>
    <ul class="contact">
      <li><span class="contact__key">E</span><span>Gtavgreg@TavenerAdvisory.net</span></li>
      <li><span class="contact__key">W</span><span>www.TavenerAdvisory.net</span></li>
      <li><span class="contact__key">M</span><span>+65 8456-0000</span></li>
    </ul>
    <p class="role role--stacked">Executive Coach<br>&amp;<br>Leadership Trainer</p>
    <p class="tagline">The Psychology of Executive Excellence</p>
  </section>

  <section class="card card--front" aria-label="Card front">
    <div class="brand">
      <span class="brand__mark"></span>
      <span class="brand__name">Tavener Growth Advisory</span>
    </div>
    <p class="role role--headline">Executive Coach &amp; Leadership Trainer</p>
    <p class="tagline">The Psychology of Executive Excellence</p>
  </section>
</body>
</html>
```